Drinking and Driving course for the courts

Sophisitcated tri-fold brochure seen by judges, lawyers etc. People taking this course have been charged with drinking and driving (alcohol). Should be classy and upmarket. Please be creative like original brochure. Please use exact wording and in same order as brochure. Also please keep in approximately same place on brochure. Spelling and grammar should be exactly same as this document is already proof-read and checked by experts.

Target Market(s)

Judges, lawyers, court system.

Industry/Entity Type

Legal

Font styles to use
Serif

Requirements
Must have
• Creative and classy. Can look similar or same as original brochure. Should have pciture/graphic of car keys and drink
Nice to have
• A background graphic like in original brochure comes across very well. Subtle etc.
Should not have
• Does not need to have pictures of vehicles/cars. Definitely no brand names of cars or alcohol labels (or any kind).

```html
<!DOCTYPE html>
<html lang="en">
<head>
<meta charset="utf-8">
<title>Drive Clear – Tri-fold Brochure</title>
<link href="https://fonts.googleapis.com/css2?family=Arimo:wght@400;700&family=Oswald:wght@400;500;700&display=swap" rel="stylesheet">
<style>
  :root {
    --backdrop: #3a3b3d;
    --navy: #14305f;
    --gold: #d4ae2c;
    --paper-top: #f4f5f6;
    --paper-mid: #c9c6b8;
    --paper-bottom: #d8b532;
    --frame: #8a6a3a;
    --white: #ffffff;
  }
  * { box-sizing: border-box; margin: 0; padding: 0; }
  html, body { width: 1200px; height: 1091px; overflow: hidden; }
  body {
    background: var(--backdrop);
    font-family: "Arimo", Arial, sans-serif;
    display: flex; align-items: center; justify-content: center;
  }
  .brochure {
    width: 1140px; height: 881px;
    display: flex;
    box-shadow: 0 10px 30px rgba(0,0,0,.45);
  }
  .panel {
    position: relative;
    width: 380px; height: 100%;
    background: linear-gradient(180deg, var(--paper-top) 0%, #e6e6e2 22%, var(--paper-mid) 52%, var(--paper-bottom) 100%);
    overflow: hidden;
  }
  .panel + .panel { border-left: 1px solid rgba(0,0,0,.08); }

  /* Background panel */
  .background-panel { padding: 42px 30px 0 34px; color: var(--navy); }
  .section-title { font-size: 34px; font-weight: 400; letter-spacing: .5px; }
  .title-rule { margin: 6px 0 22px; width: 285px; border-top: 2px solid var(--gold); border-bottom: 1px solid var(--navy); height: 5px; }
  .background-panel p { font-size: 13.2px; line-height: 1.42; margin-bottom: 20px; }

  /* Centre panel */
  .info-panel { color: var(--navy); text-align: center; }
  .quote-frame {
    position: absolute; left: 46px; top: 60px; width: 290px; height: 400px;
    border: 1px solid var(--frame);
  }
  .quote-frame.tilted { transform: rotate(-6deg); }
  .quote-frame.straight { transform: rotate(2deg); left: 42px; }
  .quote {
    position: absolute; left: 66px; top: 108px; width: 250px;
    font-size: 31px; line-height: 1.3; letter-spacing: .3px;
  }
  .contact-block { position: absolute; left: 0; right: 0; top: 525px; }
  .contact-heading { font-size: 27px; letter-spacing: 1px; margin-bottom: 26px; }
  .contact-block p { font-size: 15px; margin-bottom: 22px; color: #1a2b4a; }
  .contact-block .phone { font-size: 18px; }

  /* Cover panel */
  .cover-panel { text-align: center; }
  .cover-arc { position: absolute; inset: 0; }
  .cover-title {
    position: relative; margin-top: 48px;
    font-family: "Oswald", "Arial Narrow", sans-serif; font-weight: 500;
    font-size: 46px; line-height: 1.08; letter-spacing: 1px;
  }
  .cover-title .line-one { color: var(--gold); display: block; }
  .cover-title .line-two { color: var(--navy); display: block; font-weight: 700; }
  .cover-subtitle {
    position: relative; margin: 12px auto 0; width: 290px;
    font-family: "Oswald", sans-serif; font-size: 11.5px; line-height: 1.25;
    color: var(--navy); letter-spacing: .3px;
  }
  .school-name {
    position: absolute; left: 0; right: 0; top: 585px;
    font-family: "Oswald", sans-serif; font-weight: 700; font-size: 27px;
    color: var(--navy); letter-spacing: -.3px;
    display: flex; align-items: center; justify-content: center; gap: 10px;
  }
  .school-dot { width: 12px; height: 12px; border-radius: 50%; background: var(--navy); }
  .tagline { position: absolute; left: 0; right: 0; top: 630px; font-family: "Oswald", sans-serif; font-size: 15px; color: var(--navy); }
  .services { position: absolute; left: 0; right: 0; top: 705px; font-family: "Oswald", sans-serif; font-weight: 500; font-size: 14.5px; line-height: 1.45; color: var(--navy); }
  .cover-contacts { position: absolute; left: 0; right: 0; top: 780px; font-family: "Oswald", sans-serif; font-size: 14px; line-height: 1.4; color: var(--white); font-weight: 400; }
</style>
</head>
<body>
  <main class="brochure">
    <section class="panel background-panel">
      <h2 class="section-title">Our background:</h2>
      <div class="title-rule"></div>
      <p>Since its inception in 1998, Safe Lanes Driving School has strived to help drivers maintain their driving independence while leading safe and productive lives.&nbsp; Our motto “keeping drivers safe for good” drives our vision of helping drivers across industries and at all stages of our driving careers.</p>
      <p>Safe Lanes started out working with school boards to deliver driver training to beginner drivers. Thousands of students have graduated from our ministry-approved curriculum throughout central Ontario.&nbsp; We are also ministry-approved to instruct defensive driving (DDC) and driver improvement courses (DIC), for drivers with speeding tickets, demerit points and at fault crashes.</p>
      <p>Safe Lanes has also evolved to provide comprehensive driver rehabilitation to those who have lost, or are at risk of losing their license for medical reasons.&nbsp; This includes mobility issues requiring adaptive equipment, as well as traumatic crashes resulting in cognitive impairments and PTSD.&nbsp; We work with clients before the courts charged with impaired driving (alcohol, cannabis, opioids), road rage and stunt driving.</p>
      <p>Founder Daniel Hartley started driving at an early age on his parent’s farm.&nbsp; Driving professionally and doing so safely is in his DNA. Daniel graduated from Brookfield College School, and obtained a degree in Business and Psychology from Kingsley University.&nbsp; He is a certified in-car and in-class driving instructor and trainer.</p>
    </section>

    <section class="panel info-panel">
      <div class="quote-frame tilted"></div>
      <div class="quote-frame straight"></div>
      <p class="quote">Maintaining driving independence, while leading safe and productive lives!</p>
      <div class="contact-block">
        <h3 class="contact-heading">For more information:</h3>
        <p>www.safelanesdrivingschool.ca</p>
        <p class="phone">Call:&nbsp; 705-555-0148</p>
        <p>dhartley@safelanesdrivingschool.ca</p>
      </div>
    </section>

    <section class="panel cover-panel">
      <svg class="cover-arc" width="380" height="881" viewBox="0 0 380 881" aria-hidden="true">
        <defs>
          <linearGradient id="photoTone" x1="0" y1="0" x2="1" y2="1">
            <stop offset="0" stop-color="#8d8a84"/>
            <stop offset=".5" stop-color="#b9ad8c"/>
            <stop offset="1" stop-color="#d9a646"/>
          </linearGradient>
        </defs>
        <path d="M22,0 Q22,470 380,580" fill="none" stroke="var(--gold)" stroke-width="7"/>
      </svg>
      <h1 class="cover-title"><span class="line-one">DRIVE</span><span class="line-two">CLEAR</span></h1>
      <p class="cover-subtitle">A 1-DAY EDUCATIONAL COURSE FOR THOSE CHARGED WITH DRINKING AND DRIVING</p>
      <svg style="position:absolute;left:0;top:0" width="380" height="881" viewBox="0 0 380 881" role="img" aria-label="Photograph of car keys beside a glass of whisky on a table">
        <path d="M62,240 L380,240 L380,565 Q110,480 62,240 Z" fill="url(#photoTone)"/>
      </svg>
      <div class="school-name"><span class="school-dot"></span>Safe Lanes Driving School</div>
      <p class="tagline">Keeping drivers safe...for good!</p>
      <p class="services">For all your G License needs!<br>Beginner, Rehabilitation &amp; Remedial</p>
      <p class="cover-contacts">705-555-0148<br>www.safelanesdrivingschool.ca<br>dhartley@safelanesdrivingschool.ca</p>
    </section>
  </main>
</body>
</html>
```